New Business Cards for Organic Meat Farm

We need a business card designed for Hollowmere Farm, a meat farm in western MA. Our logo uses a hand-drawn woodcut (attached). Our color palette has been simply black and white (shown in notepad and picture of our food truck). While we are based out of western MA, we have ambitions to grow nationally, so our hope is for a classy and memorable card which will be printed on a premium quality stock from a printer like printkestrel.com.
Target Market(s)
consumers of quality meats, restauranteurs, partnering farms
Industry/Entity Type
Farming and prepared meat products
Contact Information for Business Card
Corwin Adley, President/Owner, corwin@hollowmerefarm.com, mobile: 413-555-0172, phone: 413-555-0148, hollowmerefarm.com, facebook: @hollowmerefarm, instagram: @hollowmerefarmma
Colors
Designer to choose colors to be used in the design.
Look and feel

```html
<!DOCTYPE html>
<html lang="en">
<head>
<meta charset="utf-8">
<title>Hollowmere Farm – Business Card</title>
<link href="https://fonts.googleapis.com/css2?family=Montserrat:wght@400;700&display=swap" rel="stylesheet">
<style>
  :root {
    --backdrop: #d4d4d4;
    --stock: #f1f1ee;
    --ink: #111111;
    --ink-soft: #6f6f6f;
    --rule: #d9d9d5;
  }
  * { box-sizing: border-box; margin: 0; padding: 0; }
  html, body { width: 1200px; height: 1051px; overflow: hidden; }
  body {
    background: var(--backdrop);
    font-family: "Montserrat", sans-serif;
    color: var(--ink);
    display: flex;
    flex-direction: column;
    align-items: center;
    justify-content: center;
    gap: 60px;
  }
  .card {
    width: 700px;
    height: 400px;
    background: var(--stock);
    position: relative;
    display: flex;
  }
  .brand {
    display: flex;
    flex-direction: column;
    align-items: center;
    justify-content: center;
    gap: 14px;
  }
  .brand-mark {
    width: 26px; height: 26px;
    border-radius: 50%;
    background: var(--ink);
  }
  .brand-name {
    font-weight: 700;
    font-size: 28px;
    letter-spacing: 0.1em;
    text-transform: uppercase;
    text-align: center;
    line-height: 1.25;
  }
  .card-front .brand { width: 46%; }
  .divider {
    width: 1px;
    background: var(--rule);
    margin: 60px 0;
  }
  .contact {
    flex: 1;
    padding: 70px 0 0 40px;
  }
  .contact-name {
    font-weight: 700;
    font-size: 22px;
    letter-spacing: 0.04em;
    text-transform: uppercase;
  }
  .contact-title {
    font-size: 17px;
    color: var(--ink-soft);
    margin-top: 4px;
    margin-bottom: 26px;
  }
  .contact-list { list-style: none; }
  .contact-list li {
    display: flex;
    align-items: center;
    gap: 12px;
    font-size: 16px;
    color: var(--ink-soft);
    line-height: 1.65;
    white-space: nowrap;
  }
  .contact-list svg { width: 14px; height: 14px; flex: none; fill: var(--ink); }
  .card-back { justify-content: center; align-items: center; }
  .card-back .brand-name { font-size: 40px; }
</style>
</head>
<body>
  <section class="card card-front">
    <div class="brand">
      <span class="brand-mark"></span>
      <span class="brand-name">Hollowmere<br>Farm</span>
    </div>
    <div class="divider"></div>
    <div class="contact">
      <p class="contact-name">Corwin Adley</p>
      <p class="contact-title">President / Owner</p>
      <ul class="contact-list">
        <li><svg viewBox="0 0 14 14"><rect x="3" y="0.5" width="8" height="13" rx="1.5" fill="none" stroke="#111" stroke-width="1.3"/><rect x="6" y="11" width="2" height="1"/></svg>413-555-0172</li>
        <li><svg viewBox="0 0 14 14"><path d="M3 1l2.5 0 1 3-1.5 1.2a8 8 0 0 0 3.8 3.8L10 7.5l3 1V11c0 1-1 2-2 2C5.5 13 1 8.5 1 3c0-1 1-2 2-2z"/></svg>413-555-0148</li>
        <li><svg viewBox="0 0 14 14"><path d="M1 3h12v8H1z M1 3l6 4.5L13 3" fill="none" stroke="#111" stroke-width="1.3"/></svg>corwin@hollowmerefarm.com</li>
        <li><svg viewBox="0 0 14 14"><circle cx="7" cy="7" r="6" fill="none" stroke="#111" stroke-width="1.3"/><path d="M1 7h12M7 1c2.5 3 2.5 9 0 12M7 1c-2.5 3-2.5 9 0 12" fill="none" stroke="#111" stroke-width="1"/></svg>www.hollowmerefarm.com</li>
        <li><svg viewBox="0 0 14 14"><rect x="1" y="1" width="12" height="12" rx="2"/></svg>@hollowmerefarm</li>
        <li><svg viewBox="0 0 14 14"><circle cx="7" cy="7" r="6"/></svg>@hollowmerefarmma</li>
      </ul>
    </div>
  </section>

  <section class="card card-back">
    <div class="brand">
      <span class="brand-mark"></span>
      <span class="brand-name">Hollowmere<br>Farm</span>
    </div>
  </section>
</body>
</html>
```